****Business Card Design for Cormwell Development. Design based around attached logo/company name

I’m looking for business card design for my company Cormwell Development Group,LLC. Design should be professional, sharp and minimal. Outside of the attached logos, greyscale colors for remainder of cards. My thoughts are two-sided card with attached logo on one side and my info on the other but open to one-sided as well with right design.
Target Market(s)
Real estate professionals including banks, private investors, property owners, developers, commercial tenants like Brewlantic, Granvey or Tamsett’s.
Industry/Entity Type
Commercial real estate development and investments.
Contact Information for Business Card
Name, title, email, phone #’s, web address and physical address
Font styles to use
Other font styles liked:
- Helvetica, Garamond, etc
Colors
Designer to choose only greyscale colors for use in the design.
Requirements
Must have
- Attached logo first or second options.
Nice to have
- Two sided card with logo on one side. Attached Logo/company name can be laid out any way that flows as long as it’s legible.name
Should not have
- No loud colors. ***Please do not include logo, I have removed the company design with a logo image.

```html
<!DOCTYPE html>
<html lang="en">
<head>
<meta charset="utf-8">
<title>Cormwell Development Group – Business Card</title>
<link href="https://fonts.googleapis.com/css2?family=EB+Garamond:ital,wght@0,400;1,400&display=swap" rel="stylesheet">
<style>
  :root {
    --backdrop: #d9d9d9;
    --card: #59637a;
    --ink: #e6e8ee;
    --ink-soft: #c9cdd7;
  }
  * { box-sizing: border-box; margin: 0; padding: 0; }
  html, body {
    width: 1200px; height: 846px; overflow: hidden;
    background: var(--backdrop);
    font-family: "EB Garamond", Garamond, Georgia, serif;
  }
  .sheet {
    position: relative; width: 1200px; height: 846px;
    display: flex; align-items: center; justify-content: center; gap: 48px;
  }
  .card {
    position: relative; width: 525px; height: 300px;
    background: var(--card); color: var(--ink);
    box-shadow: 0 10px 24px rgba(0,0,0,0.18);
  }
  /* Info side */
  .card--info { padding: 62px 0 0 66px; }
  .person__name { font-size: 27px; font-weight: 400; line-height: 1; letter-spacing: 0.3px; }
  .person__title { font-style: italic; font-size: 19px; margin: 6px 0 0 22px; color: var(--ink-soft); }
  .contacts { list-style: none; margin: 22px 0 0 36px; }
  .contacts li {
    display: flex; align-items: center; gap: 12px;
    font-size: 18px; line-height: 25px;
  }
  .contacts svg { width: 17px; height: 17px; flex: none; fill: none; stroke: var(--ink); stroke-width: 1.6; }
  .contacts .address { align-items: flex-start; margin-top: 12px; line-height: 21px; }
  .contacts .address svg { margin-top: 2px; fill: var(--ink); stroke: none; }
  /* Company side */
  .card--company { display: flex; align-items: center; justify-content: center; }
  .company__name { font-size: 30px; font-weight: 400; line-height: 1.2; color: var(--ink); }
</style>
</head>
<body>
<main class="sheet">
  <section class="card card--info" aria-label="Contact side">
    <h1 class="person__name">Daniel Harwick</h1>
    <p class="person__title">Title</p>
    <ul class="contacts">
      <li>
        <svg viewBox="0 0 20 20" aria-hidden="true"><path d="M5 2.5l3 3-1.8 2a10 10 0 0 0 6.3 6.3l2-1.8 3 3-2 2.3C9 16.5 3.5 11 2.7 4.5z"/></svg>
        555-0142-7730
      </li>
      <li>
        <svg viewBox="0 0 20 20" aria-hidden="true"><rect x="2" y="4.5" width="16" height="11"/><path d="M2 4.5l8 6.5 8-6.5"/></svg>
        dharwick@cormwelldev.com
      </li>
      <li>
        <svg viewBox="0 0 20 20" aria-hidden="true"><circle cx="10" cy="10" r="8"/><ellipse cx="10" cy="10" rx="3.5" ry="8"/><path d="M2 10h16M3.5 6h13M3.5 14h13"/></svg>
        www.cormwelldev.com
      </li>
      <li class="address">
        <svg viewBox="0 0 20 20" aria-hidden="true"><path d="M10 1a6.5 6.5 0 0 0-6.5 6.5C3.5 12 10 19 10 19s6.5-7 6.5-11.5A6.5 6.5 0 0 0 10 1zm0 9a2.6 2.6 0 1 1 0-5.2 2.6 2.6 0 0 1 0 5.2z"/></svg>
        <span>4180 Larkspur Lane NE<br>Atlanta, GA 30309</span>
      </li>
    </ul>
  </section>

  <section class="card card--company" aria-label="Company side">
    <p class="company__name">Cormwell Development Group, LLC</p>
  </section>
</main>
</body>
</html>
```